Crossfield Holiday Institute needs a webpage design

The worldwide first Crossfield Holiday Institute of the arts - Grenzenlose Ferienschule der Gestalter (in German) - short - GFOW needs a wepage design.
We already have a logo and would need a innovative and dynamic web design in order to be able to launch our website. The website will be our primary marketing tool, so the design should reflect the academy´s mission:
- GFOW offers young artists an experimental platform for experimenting and launching interdisciplinary projects under the guidance of established international artists. GFOW is the future!
Quick facts of the academy:
- worlwide first Crossfield Holiday Institute for professional young artists representing the fine arts: music, dance, literature, visual arts and theatre and not older than 35 years old
- two week long master classes under the guidance of established artists
- set in the beautiful Swiss Alps

Target Market(s)

young artists up to 35 years old

Industry/Entity Type

Artists

Requirements
Must have
• The design should:
- reflect the creed of the academy: GFOW is the future!
- the website will be run in 3 languages: DE, EN and FR, so the simpler the better and cheaper to run
- website needs to include the feature of an digital application from so the applicants can apply online
Nice to have
• Dynamic, flip and turn features to reach the second page
Should not have
• If possible not a traditional design, but futuristic

```html
<!DOCTYPE html>
<html lang="en">
<head>
<meta charset="utf-8">
<title>GFOW – Crossfield Holiday Institute</title>
<link href="https://fonts.googleapis.com/css2?family=Yanone+Kaffeesatz:wght@400;600&family=Arimo&display=swap" rel="stylesheet">
<style>
  :root {
    --plum: #8e2f88;
    --slate: #646e70;
    --mist: #a9b0b2;
    --paper: #ffffff;
    --edge: #e4e4e4;
    --rule: #dddddd;
    --fine: #555555;
  }
  * { margin: 0; padding: 0; box-sizing: border-box; }
  html, body { width: 1200px; height: 878px; overflow: hidden; }
  body {
    position: relative;
    background: radial-gradient(ellipse 60% 62% at 50% 50%, var(--paper) 55%, #f4f4f4 80%, var(--edge) 100%);
    font-family: "Yanone Kaffeesatz", "Arial Narrow", sans-serif;
    color: var(--slate);
  }
  .brand {
    position: absolute; left: 171px; top: 72px;
    display: flex; flex-direction: column; gap: 4px;
  }
  .brand-row { display: flex; align-items: center; gap: 12px; }
  .brand-square { width: 42px; height: 42px; background: var(--plum); border-radius: 4px; }
  .brand-name { font-size: 64px; font-weight: 600; color: var(--plum); line-height: 1; letter-spacing: 1px; }
  .brand-sub { font-family: "Arimo", Arial, sans-serif; font-size: 11px; color: var(--slate); width: 200px; line-height: 1.3; letter-spacing: .5px; }

  .headline { position: absolute; left: 516px; top: 88px; text-transform: uppercase; font-weight: 600; line-height: 1; }
  .headline .line1 { font-size: 27px; color: var(--slate); }
  .headline .line1 .soft { color: var(--mist); font-weight: 400; }
  .headline .line2 { font-size: 42px; color: var(--slate); margin-top: 2px; }
  .headline .line2 .accent { color: var(--plum); }

  .main-nav { position: absolute; left: 176px; top: 408px; list-style: none; }
  .main-nav li { font-size: 27px; line-height: 42px; display: flex; align-items: center; gap: 8px; color: var(--slate); }
  .main-nav li::before { content: ""; width: 6px; height: 6px; background: var(--slate); display: block; }

  .hero { position: absolute; left: 400px; top: 240px; width: 640px; height: 450px; }
  .hero-word {
    position: absolute; left: 10px; top: 80px; width: 620px; text-align: center;
    font-size: 330px; font-weight: 600; line-height: 1; color: var(--plum); letter-spacing: 6px;
  }
  .bubble {
    position: absolute; background: var(--paper); border: 8px solid var(--plum);
    border-radius: 14px; font-size: 34px; color: var(--slate); text-align: center;
  }
  .bubble-top { left: 50px; top: 16px; width: 200px; height: 100px; line-height: 82px; transform: rotate(5deg); }
  .bubble-bottom { left: 86px; top: 366px; width: 168px; height: 66px; line-height: 50px; border-color: var(--slate); font-size: 28px; transform: rotate(-4deg); }
  .apply {
    position: absolute; left: 300px; top: 84px; width: 72px; height: 72px; border-radius: 50%;
    background: var(--plum); color: var(--paper); font-size: 25px; line-height: 72px; text-align: center;
    box-shadow: 0 0 0 5px #dcdcdc; text-decoration: none;
  }

  .site-footer { position: absolute; left: 177px; top: 822px; width: 843px; border-top: 1px dotted var(--rule); }
  .copyright { position: absolute; left: 2px; top: 20px; font-family: "Arimo", Arial, sans-serif; font-size: 10px; color: var(--fine); }
  .social { position: absolute; right: 14px; top: 20px; display: flex; gap: 8px; }
  .social span { width: 15px; height: 15px; border-radius: 50%; background: #b3b3b3; display: block; }
</style>
</head>
<body>
  <header>
    <div class="brand">
      <div class="brand-row">
        <span class="brand-square"></span>
        <span class="brand-name">gfow</span>
      </div>
      <p class="brand-sub">Grenzenlose Ferienschule der Gestalter</p>
    </div>
    <h1 class="headline">
      <div class="line1"><span class="soft">The worldwide</span> first Crossfield</div>
      <div class="line2"><span class="accent">Holiday Institute</span> for the arts</div>
    </h1>
  </header>

  <ul class="main-nav">
    <li>About</li>
    <li>Public Attendence</li>
    <li>Sponsor &amp; Partners</li>
  </ul>

  <section class="hero">
    <div class="hero-word">gfow</div>
    <div class="bubble bubble-top">Crossfield</div>
    <div class="bubble bubble-bottom">Holiday Institute</div>
    <a class="apply" href="#apply">Apply</a>
  </section>

  <footer class="site-footer">
    <p class="copyright">© 2013 GFOW.COM. ALL RIGHTS RESERVED.</p>
    <div class="social"><span></span><span></span><span></span></div>
  </footer>
</body>
</html>
```